Lead Sales Portal Needs to Generate B2B Signup's

We are looking for banner ad designs to drive new business (B2B) traffic to our insurance and mortgage industry self serve lead sites. The sites are HomeLoanProspectHub.com and CoverageProspectHub.com, and we service over 45,000 insurance agents and mortgage lenders in a self serve lead portal model. We want our banners to generate more of these clients.

Our clients come to our sites, browse our database and then pick out and purchase the consumer leads that they need to generate new business.

We advertise extensively on Zorvix and on other PPC platforms, and our existing banners are looking really tired.

Some of the ad copy that works well for us is:

Cherry Pick Your Life Leads - Why Pay More Than $3.50 For Life Insurance Leads?
Sign up today and we'll match up to $250

Agents - Here's $250 For New Clients. Cherry Pick Your Life Insurance Leads & Save! Sign up today and we'll match up to $250

One of our Landing Pages that performs well is here:
http://www.coverageprospecthub.com/lp/008/

One of our competitors ad's are here:

http://www.tralvo.com/search/results?q=PolicyBeacon&ad=427360

We're looking for a design that is eye catching, uses our "Deeply Discounted Leads" and our "$250 match bonus"

This is the second contest that we have for the same sites. The previous designs were great and really performed well, so we are looking for new designs now that 6 months have passed. I have uploaded some winning banners from the last group for your information.
Updates

Project Deadline Extended
Reason: I've been asked by some of the designers to delay a day to get their designs in. I'm happy to do it!

Target Market(s)

These are insurance agents and mortgage lenders. All of our clients are business' or individuals within the business. This is a B2B campaign, so we need something that is professional and upscale. These are NOT consumer facing ad's!

Industry/Entity Type

Insurance

Font styles to use
Sans Serif

Requirements
Must have
• We must have the logos for the sites in the banners. Also, we must have a call to action arrow and "Go" button. Some animation is necessary, (especially around the arrow and the GO button).

One or two designs.

File type

.JPEG
.JPG
.PNG
.GIF

File size

150 KB or smaller

Image sizes

Vertical rectangle: 240 x 400
Mobile leaderboard: 320 x 50
Banner: 468 x 60
Leaderboard: 728 x 90
Square: 250 x 250
Small square: 200 x 200
Large rectangle: 336 x 280
Inline rectangle: 300 x 250
Skyscraper: 120 x 600
Wide skyscraper: 160 x 600
Half-page: 300 x 600
Large leaderboard: 970 x 90

```html
<!DOCTYPE html>
<html lang="en">
<head>
<meta charset="utf-8">
<title>Coverage Prospect Hub – Banner Set</title>
<link href="https://fonts.googleapis.com/css2?family=Arimo:wght@400;700&family=Open+Sans:wght@400;600&family=Tinos&display=swap" rel="stylesheet">
<style>
  :root {
    --navy: #0c1a6b;
    --slate: #5c6465;
    --band: #1b1d1f;
    --yellow: #f3ee1e;
    --white: #ffffff;
    --ink: #151515;
    --go-red: #e3141b;
    --go-light: #fff56a;
    --go-dark: #e2b300;
    --photo-light: #d4fbf3;
    --photo-mid: #8fe3da;
    --photo-deep: #4aa7c4;
    --note: #141618;
  }
  * { box-sizing: border-box; margin: 0; padding: 0; }
  html, body { width: 1200px; height: 1011px; overflow: hidden; background: var(--navy); }
  .board {
    position: relative; width: 1024px; height: 863px;
    transform: scale(1.171875); transform-origin: 0 0;
    font-family: "Arimo", Arial, sans-serif;
  }
  .banner {
    position: absolute; background: var(--slate); overflow: hidden;
    box-shadow: 3px 4px 8px rgba(0,0,0,.55);
  }
  .banner > * { position: absolute; }
  .photo {
    background: radial-gradient(ellipse at 55% 35%, var(--photo-light) 0%, var(--photo-mid) 55%, var(--photo-deep) 100%);
  }
  .logo { display: flex; align-items: center; gap: 4px; white-space: nowrap; z-index: 1; }
  .logo-mark { border-radius: 50%; background: var(--ink); flex: none; }
  .logo-name { font-family: "Open Sans", Arial, sans-serif; font-weight: 400; color: var(--ink); }
  .headline {
    color: var(--yellow); font-weight: 700; text-align: center; text-transform: uppercase;
    text-shadow: -1px -1px 0 #3a3a20, 1px -1px 0 #3a3a20, -1px 1px 0 #3a3a20, 1px 1px 0 #3a3a20;
  }
  .trapezoid {
    background: var(--band); color: var(--white); text-align: center; white-space: nowrap;
    display: flex; flex-direction: column; justify-content: center; line-height: 1.2;
    clip-path: polygon(6% 0, 94% 0, 100% 100%, 0 100%);
  }
  .trapezoid .accent { color: var(--yellow); font-weight: 700; }
  .discount {
    background: var(--band); color: var(--yellow); font-weight: 700; text-align: center;
    display: flex; align-items: center; justify-content: center; white-space: nowrap;
  }
  .go-button {
    border-radius: 50%; border: 1px solid #7a5a00; z-index: 2;
    background: radial-gradient(ellipse at 50% 30%, var(--go-light) 0%, #ffe21c 55%, var(--go-dark) 100%);
    display: flex; align-items: center; justify-content: center; gap: 2%;
    color: var(--go-red); font-weight: 700; line-height: 1;
    animation: go-pulse 1.2s ease-in-out infinite;
  }
  .go-button svg { height: 42%; width: auto; animation: arrow-nudge 1.2s ease-in-out infinite; }
  @keyframes go-pulse { 50% { filter: brightness(1.12); } }
  @keyframes arrow-nudge { 50% { transform: translateX(3px); } }

  /* Half-page */
  .half-page { left: 27px; top: 27px; width: 300px; height: 598px; }
  .half-page .photo { left: 3px; top: 20px; width: 295px; height: 343px; border-radius: 148px 148px 0 0; }
  .half-page .logo { left: 24px; top: 10px; }
  .half-page .logo-mark { width: 40px; height: 40px; }
  .half-page .logo-name { font-size: 18px; }
  .half-page .headline { left: 0; top: 278px; width: 100%; font-size: 28px; line-height: 32px; }
  .half-page .why { left: 0; top: 363px; width: 300px; height: 44px; font-size: 17px; }
  .half-page .discount { left: 0; top: 431px; width: 300px; height: 42px; font-size: 22px; }
  .half-page .signup { left: 0; top: 496px; width: 300px; height: 46px; font-size: 17px; }
  .half-page .go-button { left: 101px; top: 553px; width: 100px; height: 36px; font-size: 24px; }

  /* Vertical rectangle */
  .vertical { left: 354px; top: 144px; width: 240px; height: 399px; }
  .vertical .photo { left: 3px; top: 16px; width: 235px; height: 230px; border-radius: 118px 118px 0 0; }
  .vertical .logo { left: 20px; top: 10px; }
  .vertical .logo-mark { width: 33px; height: 33px; }
  .vertical .logo-name { font-size: 14px; }
  .vertical .headline { left: 0; top: 193px; width: 100%; font-size: 21px; line-height: 25px; }
  .vertical .why { left: 0; top: 251px; width: 240px; height: 34px; font-size: 14px; }
  .vertical .discount { left: 0; top: 296px; width: 240px; height: 27px; font-size: 17px; }
  .vertical .signup { left: 0; top: 333px; width: 240px; height: 33px; font-size: 14px; }
  .vertical .go-button { left: 79px; top: 369px; width: 82px; height: 28px; font-size: 19px; }

  /* Square */
  .square { left: 631px; top: 294px; width: 250px; height: 250px; }
  .square .photo { left: 2px; top: 16px; width: 245px; height: 148px; border-radius: 122px 122px 0 0; }
  .square .logo { left: 40px; top: 3px; }
  .square .logo-mark { width: 30px; height: 30px; }
  .square .logo-name { font-size: 12px; }
  .square .headline { left: 0; top: 113px; width: 100%; font-size: 21px; line-height: 23px; }
  .square .why { left: 12px; top: 166px; width: 210px; height: 27px; font-size: 11px; }
  .square .discount { left: 12px; top: 195px; width: 224px; height: 22px; font-size: 14px; }
  .square .signup { left: 6px; top: 219px; width: 168px; height: 28px; font-size: 12px; }
  .square .go-button { left: 177px; top: 221px; width: 68px; height: 26px; font-size: 17px; }

  /* Banner 468 */
  .banner-468 { left: 354px; top: 578px; width: 468px; height: 60px; }
  .banner-468 .photo { left: 2px; top: 2px; width: 118px; height: 56px; border-radius: 28px 0 0 28px; }
  .banner-468 .headline { left: 124px; top: 12px; width: 138px; font-size: 13px; line-height: 18px; text-shadow: none; }
  .banner-468 .why { left: 261px; top: 2px; width: 130px; height: 21px; font-size: 8.5px; }
  .banner-468 .discount { left: 263px; top: 24px; width: 125px; height: 13px; font-size: 8px; }
  .banner-468 .signup { left: 276px; top: 39px; width: 100px; height: 19px; font-size: 7px; }
  .banner-468 .logo { left: 393px; top: 5px; gap: 2px; }
  .banner-468 .logo-mark { width: 12px; height: 12px; }
  .banner-468 .logo-name { font-size: 5.5px; }
  .banner-468 .go-button { left: 409px; top: 22px; width: 50px; height: 20px; font-size: 12px; }

  /* Large leaderboard */
  .leaderboard { left: 27px; top: 665px; width: 970px; height: 90px; }
  .leaderboard .photo { left: 2px; top: 2px; width: 118px; height: 86px; border-radius: 43px 0 0 43px; }
  .leaderboard .headline { left: 124px; top: 18px; width: 224px; font-size: 22px; line-height: 28px; text-shadow: none; }
  .leaderboard .why { left: 358px; top: 3px; width: 270px; height: 44px; font-size: 16px; }
  .leaderboard .discount { left: 343px; top: 50px; width: 290px; height: 37px; font-size: 19px;
    clip-path: polygon(5% 0, 95% 0, 100% 100%, 0 100%); }
  .leaderboard .logo { left: 664px; top: 9px; }
  .leaderboard .logo-mark { width: 32px; height: 32px; }
  .leaderboard .logo-name { font-size: 14px; }
  .leaderboard .signup { left: 641px; top: 48px; width: 248px; height: 39px; font-size: 16px; }
  .leaderboard .go-button { left: 876px; top: 28px; width: 80px; height: 30px; font-size: 20px; }

  .note {
    position: absolute; left: 57px; top: 778px; width: 926px; height: 70px; background: var(--note);
    color: var(--white); font-family: "Tinos", "Times New Roman", serif; font-size: 30px;
    letter-spacing: 2px; white-space: nowrap;
    display: flex; align-items: center; justify-content: center;
  }
</style>
</head>
<body>
<div class="board">

  <section class="banner half-page">
    <div class="photo" role="img" aria-label="Photo of a businesswoman talking on the phone"></div>
    <div class="logo"><span class="logo-mark"></span><span class="logo-name">Coverage Prospect Hub</span></div>
    <h2 class="headline">Cherry Pick Your<br>Life Leads</h2>
    <p class="trapezoid why"><span>- Why Pay More Than $3.50</span><span>For Life Insurance Leads?</span></p>
    <p class="discount">"Deeply Discounted Leads"</p>
    <p class="trapezoid signup"><span>Sign up today and</span><span class="accent">we'll match up to $250</span></p>
    <a class="go-button">GO<svg viewBox="0 0 20 12"><path d="M0 4h12V0l8 6-8 6V8H0z" fill="#111"/></svg></a>
  </section>

  <section class="banner vertical">
    <div class="photo" role="img" aria-label="Photo of a businesswoman talking on the phone"></div>
    <div class="logo"><span class="logo-mark"></span><span class="logo-name">Coverage Prospect Hub</span></div>
    <h2 class="headline">Cherry Pick Your<br>Life Leads</h2>
    <p class="trapezoid why"><span>- Why Pay More Than $3.50</span><span>For Life Insurance Leads?</span></p>
    <p class="discount">"Deeply Discounted Leads"</p>
    <p class="trapezoid signup"><span>Sign up today and</span><span class="accent">we'll match up to $250</span></p>
    <a class="go-button">GO<svg viewBox="0 0 20 12"><path d="M0 4h12V0l8 6-8 6V8H0z" fill="#111"/></svg></a>
  </section>

  <section class="banner square">
    <div class="photo" role="img" aria-label="Photo of a businesswoman talking on the phone"></div>
    <div class="logo"><span class="logo-mark"></span><span class="logo-name">Coverage Prospect Hub</span></div>
    <h2 class="headline">Cherry Pick Your<br>Life Leads</h2>
    <p class="trapezoid why"><span>- Why Pay More Than $3.50</span><span>For Life Insurance Leads?</span></p>
    <p class="discount">"Deeply Discounted Leads"</p>
    <p class="trapezoid signup"><span>Sign up today and</span><span class="accent">we'll match up to $250</span></p>
    <a class="go-button">GO<svg viewBox="0 0 20 12"><path d="M0 4h12V0l8 6-8 6V8H0z" fill="#111"/></svg></a>
  </section>

  <section class="banner banner-468">
    <div class="photo" role="img" aria-label="Photo of a businesswoman talking on the phone"></div>
    <h2 class="headline">Cherry Pick Your<br>Life Leads</h2>
    <p class="trapezoid why"><span>- Why Pay More Than $3.50</span><span>For Life Insurance Leads?</span></p>
    <p class="discount">"Deeply Discounted Leads"</p>
    <p class="trapezoid signup"><span>Sign up today and</span><span class="accent">we'll match up to $250</span></p>
    <div class="logo"><span class="logo-mark"></span><span class="logo-name">Coverage Prospect Hub</span></div>
    <a class="go-button">GO<svg viewBox="0 0 20 12"><path d="M0 4h12V0l8 6-8 6V8H0z" fill="#111"/></svg></a>
  </section>

  <section class="banner leaderboard">
    <div class="photo" role="img" aria-label="Photo of a businesswoman talking on the phone"></div>
    <h2 class="headline">Cherry Pick Your<br>Life Leads</h2>
    <p class="trapezoid why"><span>- Why Pay More Than $3.50</span><span>For Life Insurance Leads?</span></p>
    <p class="discount">"Deeply Discounted Leads"</p>
    <div class="logo"><span class="logo-mark"></span><span class="logo-name">Coverage Prospect Hub</span></div>
    <p class="trapezoid signup"><span>Sign up today and</span><span class="accent">we'll match up to $250</span></p>
    <a class="go-button">GO<svg viewBox="0 0 20 12"><path d="M0 4h12V0l8 6-8 6V8H0z" fill="#111"/></svg></a>
  </section>

  <p class="note">THE GO BUTTON IS ANIMATED IN ALL OF THE BANNERS</p>

</div>
</body>
</html>
```